Prestige Car Bodyshop Business Card

We are a car bodyshop based in the UK. Our customer base is mainly prestige high-value vehicles. I am looking for a classy and stylish business card design for my staff to give out to customers, with their direct email and phone number, as well as our main email and phone number with address details

I am also looking to have a general business card design with just our main company address and contact details, but also have a space to add a manufacturer approval logo (i.e Velmora, Orek, Tovalo etc... logo) in the corner somewhere.

I do not particularly want any outlines or pictures of cars on the card, I would just like a quality high-end look.

Please feel free to get in touch if you have any questions or queries?

Many Thanks

Malcolm

Target Market(s)

Prestige vehicle owners

Industry/Entity Type

Automotive

Contact Information for Business Card

I am looking for a classy and stylish business card design for my staff to give out to customers, with their direct email and phone number, as well as our main email and phone number with address details

Font styles to use
Sans Serif

Colors

Designer to choose colors to be used in the design.

Requirements
Nice to have
• I do not particularly want any outlines or pictures of cars on the card, I would just like a quality high-end look.

```html
<!DOCTYPE html>
<html lang="en">
<head>
<meta charset="utf-8">
<title>Harlow Accident Repair Centre – Business Cards</title>
<link rel="stylesheet" href="https://fonts.googleapis.com/css2?family=Cabin:wght@400;500&family=Crimson+Text:wght@400;700&family=Open+Sans:wght@400;600&display=swap">
<style>
  :root {
    --bg: #e9ebef;
    --card: #ffffff;
    --navy: #1b3a7a;
    --navy-dark: #0f2a63;
    --orange: #e0791c;
    --ink: #1d1d1f;
    --muted: #3a3a3a;
    --photo-a: #f4f4f5;
    --photo-b: #e3e3e6;
  }
  * { box-sizing: border-box; margin: 0; padding: 0; }
  html, body { width: 1200px; height: 720px; overflow: hidden; }
  body {
    background: var(--bg);
    font-family: "Open Sans", sans-serif;
    position: relative;
  }
  .card {
    position: absolute;
    width: 540px;
    height: 310px;
    background: var(--card);
    box-shadow: 0 6px 24px rgba(20, 30, 60, .18);
    overflow: hidden;
  }
  .card--front { left: 40px; top: 205px; }
  .card--back { left: 620px; top: 205px; }

  .card-photo {
    position: absolute; inset: 0;
    background:
      radial-gradient(ellipse at 35% 70%, var(--photo-b) 0%, transparent 55%),
      radial-gradient(ellipse at 75% 40%, var(--photo-b) 0%, transparent 50%),
      linear-gradient(135deg, var(--photo-a), #ececee);
  }
  .card-bands { position: absolute; inset: 0; }
  .band { fill: var(--orange); opacity: .9; }

  /* Front */
  .brand {
    position: absolute; left: 38px; top: 70px;
    display: flex; align-items: center; gap: 18px;
  }
  .brand-dot {
    width: 104px; height: 104px; border-radius: 50%;
    background: var(--navy);
  }
  .brand-name {
    font-family: "Cabin", sans-serif; font-weight: 400;
    font-size: 44px; color: var(--navy); letter-spacing: 1px; line-height: 1;
  }
  .brand-rule { height: 2px; background: var(--navy); margin: 6px 0 5px; width: 232px; }
  .brand-tag {
    font-family: "Cabin", sans-serif; font-size: 14px;
    color: var(--navy); letter-spacing: .6px;
  }
  .approvals {
    position: absolute; left: 40px; top: 214px;
    display: grid; grid-template-columns: auto auto; gap: 8px 22px;
    font-family: "Cabin", sans-serif; font-size: 12px; color: var(--ink);
    letter-spacing: 1px; text-transform: uppercase;
  }

  /* Back */
  .back-brand {
    position: absolute; left: 22px; top: 212px;
    transform: rotate(-62deg); transform-origin: left center;
    display: flex; align-items: center; gap: 8px;
  }
  .back-brand .brand-dot { width: 46px; height: 46px; }
  .back-brand .brand-name { font-size: 24px; color: var(--navy-dark); }
  .back-brand .brand-rule { width: 108px; height: 1px; margin: 3px 0; background: var(--navy-dark); }
  .back-brand .brand-tag { font-size: 7px; color: var(--navy-dark); }

  .person {
    position: absolute; left: 236px; top: 72px;
    display: flex; gap: 12px;
  }
  .person-name {
    font-family: "Crimson Text", serif; font-size: 32px; color: var(--ink); line-height: 1;
  }
  .person-name strong { font-weight: 700; }
  .person-role { font-size: 13px; color: var(--muted); margin-top: 4px; }
  .contacts {
    position: absolute; left: 236px; top: 160px;
    list-style: none; font-size: 17px; color: var(--ink);
  }
  .contacts li { display: flex; align-items: flex-start; gap: 12px; margin-bottom: 6px; line-height: 1.3; }
  .icon { width: 18px; height: 18px; flex: none; margin-top: 3px; fill: var(--orange); }
</style>
</head>
<body>

<section class="card card--front" aria-label="Company card">
  <div class="card-photo" role="img" aria-label="Faded engine bay photograph"></div>
  <svg class="card-bands" viewBox="0 0 540 310" aria-hidden="true">
    <polygon class="band" points="292,310 348,310 478,0 422,0"/>
    <polygon class="band" points="362,310 540,310 540,0 492,0"/>
  </svg>
  <div class="brand">
    <div class="brand-dot"></div>
    <div>
      <div class="brand-name">HARLOW</div>
      <div class="brand-rule"></div>
      <div class="brand-tag">ACCIDENT REPAIR CENTRE</div>
    </div>
  </div>
  <div class="approvals">
    <span>Tovalo</span><span>Stennar</span>
    <span>Orek</span><span>Pella</span>
    <span>Velmora</span>
  </div>
</section>

<section class="card card--back" aria-label="Staff card">
  <div class="card-photo" role="img" aria-label="Faded engine bay photograph"></div>
  <svg class="card-bands" viewBox="0 0 540 310" aria-hidden="true">
    <polygon class="band" points="0,0 196,0 26,310 0,310"/>
    <polygon fill="#ffffff" opacity=".85" points="26,0 44,0 0,80 0,48"/>
  </svg>
  <div class="back-brand">
    <div class="brand-dot"></div>
    <div>
      <div class="brand-name">HARLOW</div>
      <div class="brand-rule"></div>
      <div class="brand-tag">ACCIDENT REPAIR CENTRE</div>
    </div>
  </div>

  <div class="person">
    <svg class="icon" viewBox="0 0 20 20" aria-hidden="true" style="margin-top:18px">
      <circle cx="10" cy="6" r="4.5"/><path d="M2 19c0-5 3.5-7.5 8-7.5s8 2.5 8 7.5z"/>
    </svg>
    <div>
      <div class="person-name"><strong>Daniel</strong> Ashford</div>
      <div class="person-role">Auto Electrician</div>
    </div>
  </div>

  <ul class="contacts">
    <li>
      <svg class="icon" viewBox="0 0 20 20" aria-hidden="true"><rect width="20" height="20" rx="3"/><path fill="#fff" d="M6 4l2.5 3-1.3 1.5c.8 1.7 2 2.9 3.6 3.6L12.3 11l3 2.5-1.2 2.3C9 15.5 4.5 11 4.2 5.8z"/></svg>
      <span>+ 44 20 7946 0321</span>
    </li>
    <li>
      <svg class="icon" viewBox="0 0 20 20" aria-hidden="true"><rect y="3" width="20" height="14" rx="2"/><path fill="none" stroke="#fff" stroke-width="1.6" d="M1.5 5l8.5 6.5L18.5 5"/></svg>
      <span>electrician@harlowrepair.com</span>
    </li>
    <li>
      <svg class="icon" viewBox="0 0 20 20" aria-hidden="true"><path d="M10 1a6 6 0 0 0-6 6c0 4.5 6 12 6 12s6-7.5 6-12a6 6 0 0 0-6-6zm0 8.3A2.3 2.3 0 1 1 10 4.7a2.3 2.3 0 0 1 0 4.6z"/></svg>
      <span>12 Alder Row<br>London</span>
    </li>
  </ul>
</section>

</body>
</html>
```